Prairie Kettle Billboard

We are looking to have a new billboard design for our Casual Restaurant chain. We are a steakhouse chain that is very casual. You can visit our website at: www.prairiekettle-demo.net to get an idea of our menu. We are looking to have some new billboard ideas for our steakhouse so that we can communicate our concept to customers that are passing by the billboard. I have attached some items to give you a feel for our concept. The Billboard will be 14'X48'. I look forward to hearing from you. Glen

```html
<!DOCTYPE html>
<html lang="en">
<head>
<meta charset="utf-8">
<title>Prairie Kettle Billboard</title>
<link rel="stylesheet" href="https://fonts.googleapis.com/css2?family=Rubik+Dirt&family=Sacramento&display=swap">
<style>
  :root {
    --backdrop: #d8d8d5;
    --board-dark: #0d0d0d;
    --board-mid: #2a2928;
    --ink-cream: #ece8d6;
    --pick-light: #f1d9c4;
    --pick-mid: #c99f86;
    --pick-shadow: #5a4a42;
    --brand-red: #c8231d;
  }
  * { margin: 0; padding: 0; box-sizing: border-box; }
  html, body {
    width: 1200px;
    height: 689px;
    overflow: hidden;
    background: var(--backdrop);
  }
  .billboard {
    position: absolute;
    left: 40px;
    top: 135px;
    width: 1120px;
    height: 419px;
    overflow: hidden;
    background:
      radial-gradient(ellipse 55% 80% at 30% 55%, var(--board-mid) 0%, var(--board-dark) 75%);
  }
  .toothpick-burst {
    position: absolute;
    left: 75px;
    top: 50px;
    width: 320px;
    height: 320px;
    border-radius: 50%;
    background:
      radial-gradient(circle at 50% 50%, var(--pick-shadow) 0%, var(--pick-mid) 22%, var(--pick-light) 55%, rgba(241,217,196,0.35) 80%, rgba(241,217,196,0) 100%);
  }
  .headline {
    position: absolute;
    left: 530px;
    top: 35px;
    color: var(--ink-cream);
    font-weight: 400;
    white-space: nowrap;
  }
  .headline-script {
    display: block;
    font-family: "Sacramento", cursive;
    font-size: 90px;
    line-height: 1;
    margin-left: 30px;
  }
  .headline-main {
    display: block;
    font-family: "Rubik Dirt", sans-serif;
    font-size: 100px;
    line-height: 1;
    margin-top: -14px;
    letter-spacing: 2px;
  }
  .brand {
    position: absolute;
    left: 850px;
    top: 250px;
    display: flex;
    flex-direction: column;
    align-items: center;
    gap: 8px;
    color: var(--ink-cream);
    font-family: "Rubik Dirt", sans-serif;
  }
  .brand-lockup {
    display: flex;
    align-items: center;
    gap: 10px;
    white-space: nowrap;
  }
  .brand-dot {
    width: 24px;
    height: 24px;
    border-radius: 50%;
    background: var(--brand-red);
    flex: none;
  }
  .brand-name {
    font-size: 26px;
    line-height: 1;
  }
  .brand-tagline {
    font-size: 14px;
    line-height: 1;
    letter-spacing: 3px;
    white-space: nowrap;
  }
</style>
</head>
<body>
  <main class="billboard">
    <div class="toothpick-burst" role="img" aria-label="Photo of a bundle of wooden toothpicks fanned out into a round burst"></div>
    <h1 class="headline">
      <span class="headline-script">toothpicks</span>
      <span class="headline-main">included</span>
    </h1>
    <div class="brand">
      <div class="brand-lockup">
        <span class="brand-dot"></span>
        <span class="brand-name">Prairie Kettle</span>
      </div>
      <p class="brand-tagline">GRILL &amp; SALOON</p>
    </div>
  </main>
</body>
</html>
```